Consulting firm needs elegant, modern designs

Business card design - I have a logo which has previously been developed for Q-Pathways - I will attach. I will also attach specifications for the size of the business card.

We also need a logo design for our leadership consulting product - Form in Guidance - we focus on improving workplace health by educating leaders and learning professionals about how the physical and emotional affects performance and engagement. I have some example logos and ideas which I will attach - these have attempted to bring in the body but I do not like the font (see www.formingguidance-example.com for preferred font). Idea is to please have a 'body' visible somehow in the word Leadership, ensuring that this conveys flexibility and agility. Colors which I prefer are deep purple OR turquoise, together with silver. COLORS below are for LOGO design.

Target Market(s)

For the business card, it should be more masculine. The logo which will be attached should be neutralized into dark blue shades and silver. The business card Q-Pathways is focused on business transformation - organizations who would require a consultant to help them enter new markets, for example.

Industry/Entity Type

Leadership

Contact Information for Business Card

Content:
Q-Pathways
Lindenkade 27
4921KP, Velmonde, The Netherlands
maurits@Q-Pathways.example
www.Q-Pathways.example

Colors for business card should be conservative and slightly more masculine. Use the Q-Pathways logo but change the colors to blue or shades of gray/black.

Dimensions for cut
85 x 55 mm
1004 x 650 pixels
Full document size
88 x 58 mm
1040 x 685 pixels
For the best result, you need to design the full document size including the bleed

Logo Text

Form in Guidance

Font styles to use
Serif
Sans Serif

Colors
876aae
333333
959595

Requirements
Must have
• Professional, modern and unique business card design
• Professional, elegant, and modern logo design - with creative thinking
Should not have
• Too many colors

```html
<!DOCTYPE html>
<html lang="en">
<head>
<meta charset="utf-8">
<title>Q-Pathways Business Card</title>
<link href="https://fonts.googleapis.com/css2?family=Lato:ital,wght@0,300;0,400;0,700;1,400&display=swap" rel="stylesheet">
<style>
  :root {
    --stage: #141216;
    --card-white: #f4f4f5;
    --card-white-shade: #e4e4e6;
    --ink: #2b2452;
    --rule: #6e62a6;
    --night-top: #2a2359;
    --night-bottom: #17132f;
    --silver: #cfd0d6;
    --silver-soft: #a9aab4;
    --accent: #4b8f9a;
  }
  * { margin: 0; padding: 0; box-sizing: border-box; }
  html, body {
    width: 1200px; height: 900px; overflow: hidden;
    background: var(--stage);
    font-family: "Lato", sans-serif;
  }
  .canvas {
    width: 1200px; height: 900px;
    display: flex; align-items: center; justify-content: center; gap: 40px;
  }
  .card {
    width: 540px; height: 350px;
    border-radius: 16px;
    position: relative;
    overflow: hidden;
    box-shadow: 0 18px 40px rgba(0,0,0,.55);
  }
  /* Front */
  .card-front {
    background: linear-gradient(135deg, var(--card-white-shade), var(--card-white) 55%, #ffffff);
    color: var(--ink);
  }
  .identity {
    position: absolute; left: 60px; top: 140px; text-align: right; width: 190px;
  }
  .identity-name { font-size: 27px; font-weight: 400; letter-spacing: .2px; }
  .identity-role { font-size: 14px; font-style: italic; margin-top: 2px; }
  .divider {
    position: absolute; left: 276px; top: 112px; width: 1px; height: 126px;
    background: var(--rule);
  }
  .contact {
    position: absolute; left: 296px; top: 116px;
    font-size: 12.5px; line-height: 20px;
  }
  .contact-company { font-weight: 700; font-size: 14px; }
  .contact-row { display: flex; align-items: center; gap: 6px; }
  .contact-row svg { width: 11px; height: 11px; fill: var(--ink); flex: none; }
  /* Back */
  .card-back {
    background: radial-gradient(circle at 70% 25%, var(--night-top), var(--night-bottom) 75%);
    color: var(--silver);
  }
  .brand {
    position: absolute; left: 48px; top: 118px;
    display: flex; align-items: center; gap: 16px;
  }
  .brand-dot { width: 56px; height: 56px; border-radius: 50%; background: var(--accent); }
  .brand-name { font-size: 56px; font-weight: 300; letter-spacing: .5px; }
  .tagline {
    position: absolute; left: 122px; top: 192px;
    font-size: 15px; font-weight: 300; color: var(--silver-soft); letter-spacing: .4px;
  }
  .product {
    position: absolute; right: 36px; bottom: 30px;
    font-size: 20px; font-weight: 300; color: var(--silver);
  }
</style>
</head>
<body>
<main class="canvas">
  <section class="card card-front" aria-label="Business card front">
    <div class="identity">
      <div class="identity-name">Joris Verhaag</div>
      <div class="identity-role">President</div>
    </div>
    <div class="divider"></div>
    <div class="contact">
      <div class="contact-company">Q-Pathways</div>
      <div>Lindenkade 27</div>
      <div>4921KP, Velmonde, The Netherlands</div>
      <div class="contact-row">
        <svg viewBox="0 0 24 24" aria-hidden="true"><path d="M6.6 10.8a15 15 0 0 0 6.6 6.6l2.2-2.2c.3-.3.7-.4 1-.2 1.1.4 2.3.6 3.6.6.6 0 1 .4 1 1V20c0 .6-.4 1-1 1A17 17 0 0 1 3 4c0-.6.4-1 1-1h3.5c.6 0 1 .4 1 1 0 1.3.2 2.5.6 3.6.1.3 0 .7-.2 1z"/></svg>
        (076) 5210 4398
      </div>
      <div class="contact-row">
        <svg viewBox="0 0 24 24" aria-hidden="true"><path d="M2 5h20v14H2z M2 5l10 8 10-8" fill="none" stroke="currentColor" stroke-width="2"/><path d="M2 5h20v2l-10 7L2 7z"/></svg>
        maurits@Q-Pathways.example
      </div>
      <div class="contact-row">
        <svg viewBox="0 0 24 24" aria-hidden="true"><path d="M12 2a10 10 0 1 0 0 20 10 10 0 0 0 0-20zm0 2c1.2 1.5 2 3.6 2.2 6H9.8C10 7.6 10.8 5.5 12 4zm-2.2 8h4.4c-.2 2.4-1 4.5-2.2 6-1.2-1.5-2-3.6-2.2-6zM4 12h3.8c.1 2 .6 3.9 1.4 5.4A8 8 0 0 1 4 12zm0-2a8 8 0 0 1 5.2-5.4C8.4 6.1 7.9 8 7.8 10zm12.2 2H20a8 8 0 0 1-5.2 5.4c.8-1.5 1.3-3.4 1.4-5.4zm0-2c-.1-2-.6-3.9-1.4-5.4A8 8 0 0 1 20 10z"/></svg>
        www.Q-Pathways.example
      </div>
    </div>
  </section>

  <section class="card card-back" aria-label="Business card back">
    <div class="brand">
      <span class="brand-dot"></span>
      <span class="brand-name">Q-Pathways</span>
    </div>
    <div class="tagline">Guiding each new move</div>
    <div class="product">Form in Guidance</div>
  </section>
</main>
</body>
</html>
```